Income Tax Flyer - Updates Needed

Just need to update this flyer design and give it a new look. We would like to keep all the same wording but make it stand out a little more. Our selling point is the "Same Day Tax Advance up to $6,000"

Industry/Entity Type

Lending, Small Loans, Tax Services, Title Loans, Personal Loans

```html
<!DOCTYPE html>
<html lang="en">
<head>
<meta charset="utf-8">
<title>Same Day Tax Advance Flyer</title>
<link href="https://fonts.googleapis.com/css2?family=Montserrat:wght@500;600;700;800&display=swap" rel="stylesheet">
<style>
  :root{
    --green:#10512f;
    --green-dark:#0c4427;
    --red:#c41e26;
    --paper:#f1f1f3;
    --white:#ffffff;
    --stage:#d9d9db;
  }
  *{box-sizing:border-box;margin:0;padding:0}
  html,body{width:675px;height:1200px;overflow:hidden;background:var(--stage);font-family:"Montserrat",Arial,sans-serif}
  .flyer{position:absolute;left:20px;top:150px;width:635px;height:900px;background:var(--paper);overflow:hidden;box-shadow:0 6px 24px rgba(0,0,0,.18)}
  .flyer-shapes{position:absolute;inset:0}
  .abs{position:absolute}

  .brand{left:30px;top:48px;display:flex;align-items:center;gap:10px;color:var(--green);font-weight:700;font-size:21px;line-height:1.1}
  .brand-mark{width:34px;height:34px;border-radius:50%;background:var(--red);flex:none}

  .contact-list{right:14px;top:22px;display:flex;flex-direction:column;gap:9px;align-items:flex-end}
  .contact-item{display:flex;align-items:center;gap:10px;color:var(--white);font-size:18px;font-weight:500;height:26px}
  .contact-item b{font-weight:700}
  .contact-icon{width:26px;height:26px;border-radius:50%;background:var(--white);display:flex;align-items:center;justify-content:center}

  .hero-copy{left:24px;top:172px;color:var(--white)}
  .hero-lead{font-size:27px;font-weight:500;line-height:36px}
  .hero-lead strong{font-weight:700}
  .hero-rule{display:inline-block;width:138px;height:2px;background:var(--white);vertical-align:middle;margin-left:12px}
  .hero-title{margin-top:8px;font-size:46px;font-weight:800;line-height:54px;letter-spacing:-.5px}

  .pitch{left:0;width:635px;top:500px;text-align:center;color:var(--red);font-size:33px;font-weight:700;line-height:40px;letter-spacing:-.3px}

  .step-label{width:180px;text-align:center;top:690px;color:var(--green);font-size:17px;font-weight:600;line-height:23px}

  .cta{left:166px;top:762px;width:300px;height:48px;border-radius:24px;background:var(--red);color:var(--white);font-size:25px;font-weight:800;display:flex;align-items:center;justify-content:center}

  .footer-phone{left:23px;top:831px;width:271px;height:45px;border:1.5px solid var(--white);border-radius:23px;display:flex;align-items:center;gap:10px;padding-left:4px;color:var(--white);font-size:29px;font-weight:700;letter-spacing:-.3px}
  .footer-phone .contact-icon{width:36px;height:36px}
  .footer-divider{left:318px;top:833px;width:1.5px;height:44px;background:var(--white)}
  .footer-address{left:340px;top:830px;display:flex;align-items:center;gap:10px;color:var(--white);font-size:13.5px;font-weight:600;line-height:18px}
  .footer-address .contact-icon{width:34px;height:34px;flex:none}
</style>
</head>
<body>
<div class="flyer">
  <svg class="flyer-shapes" width="635" height="900" viewBox="0 0 635 900">
    <defs>
      <linearGradient id="deskTone" x1="0" y1="0" x2="1" y2="1">
        <stop offset="0" stop-color="#e9eef0"/>
        <stop offset=".5" stop-color="#b9a790"/>
        <stop offset="1" stop-color="#22304a"/>
      </linearGradient>
    </defs>
    <rect x="0" y="143" width="635" height="330" fill="var(--green)"/>
    <path d="M250,0 Q222,2 231,32 L400,432 Q410,455 392,474" transform="translate(-7,0)" fill="none" stroke="var(--red)" stroke-width="13"/>
    <path d="M250,0 L635,0 L635,143 L278,143 L231,32 Q222,2 250,0 Z" fill="var(--green)"/>
    <path d="M278,143 L635,143 L635,473 L392,473 Q410,455 400,432 Z" fill="url(#deskTone)" role="img" aria-label="Photo of a businessman typing at an office desk with a tax form on the monitor"/>
    <rect x="0" y="785" width="635" height="115" fill="var(--green)"/>

    <g class="steps" stroke="var(--red)" stroke-width="1.3" fill="none">
      <line x1="23" y1="631" x2="612" y2="631"/>
      <line x1="212" y1="598" x2="212" y2="726"/>
      <line x1="423" y1="598" x2="423" y2="726"/>
    </g>
    <g class="step-badges">
      <g transform="translate(105,631)">
        <circle r="33" fill="var(--white)" stroke="var(--red)" stroke-width="1.5"/>
        <path d="M-6,683" fill="none"/>
        <path d="M-9,-14 L9,-14 L5,-8 Q16,2 10,10 L-10,10 Q-16,2 -5,-8 Z" fill="none" stroke="var(--green)" stroke-width="2"/>
        <text x="0" y="6" text-anchor="middle" font-size="11" font-weight="700" fill="var(--red)" font-family="Montserrat,sans-serif">$</text>
        <path d="M-20,16 Q-6,12 4,16 L14,10" fill="none" stroke="var(--green)" stroke-width="2"/>
        <path d="M-6,38 L6,38 L0,46 Z" fill="var(--red)"/>
      </g>
      <g transform="translate(317,631)">
        <circle r="33" fill="var(--white)" stroke="var(--red)" stroke-width="1.5"/>
        <rect x="-12" y="-16" width="22" height="28" fill="none" stroke="var(--green)" stroke-width="2"/>
        <rect x="-6" y="-12" width="22" height="28" fill="var(--white)" stroke="var(--green)" stroke-width="2"/>
        <circle cx="5" cy="2" r="5" fill="none" stroke="var(--red)" stroke-width="2"/>
        <path d="M-6,38 L6,38 L0,46 Z" fill="var(--red)"/>
      </g>
      <g transform="translate(529,631)">
        <circle r="33" fill="var(--white)" stroke="var(--red)" stroke-width="1.5"/>
        <circle cx="-2" cy="2" r="15" fill="none" stroke="var(--green)" stroke-width="2"/>
        <rect x="-6" y="-19" width="8" height="4" fill="var(--green)"/>
        <path d="M-2,2 L-2,-7 M-2,2 L5,6" stroke="var(--red)" stroke-width="2"/>
        <circle cx="11" cy="12" r="7" fill="var(--white)" stroke="var(--red)" stroke-width="2"/>
        <path d="M-6,38 L6,38 L0,46 Z" fill="var(--red)"/>
      </g>
    </g>
  </svg>

  <div class="abs brand"><span class="brand-mark"></span><span>Ledgerline<br>Financial</span></div>

  <div class="abs contact-list">
    <div class="contact-item"><b>555-014-2290</b><span class="contact-icon"><svg width="14" height="14" viewBox="0 0 24 24"><path d="M6 2l4 4-2 3c1 3 4 6 7 7l3-2 4 4-3 4C10 22 2 14 2 5z" fill="none" stroke="var(--green)" stroke-width="2"/></svg></span></div>
    <div class="contact-item"><span>www.<b>ledgerlinefin</b>.com</span><span class="contact-icon"><svg width="15" height="15" viewBox="0 0 24 24"><circle cx="12" cy="12" r="10" fill="none" stroke="var(--green)" stroke-width="2"/><path d="M2 12h20M12 2c4 4 4 16 0 20M12 2c-4 4-4 16 0 20" fill="none" stroke="var(--green)" stroke-width="2"/></svg></span></div>
    <div class="contact-item"><span>office@<b>ledgerlinefin</b>.com</span><span class="contact-icon"><svg width="15" height="15" viewBox="0 0 24 24"><rect x="2" y="5" width="20" height="14" fill="none" stroke="var(--green)" stroke-width="2"/><path d="M2 5l10 8 10-8" fill="none" stroke="var(--green)" stroke-width="2"/></svg></span></div>
  </div>

  <div class="abs hero-copy">
    <p class="hero-lead">Apply here for<br><strong>$5,000-$6,000</strong><br>today!<span class="hero-rule"></span></p>
    <h1 class="hero-title">Same Day<br>Tax Advance<br>Up to $6,000</h1>
  </div>

  <h2 class="abs pitch">File Your Taxes and Apply<br>for an Easy Advance!</h2>

  <p class="abs step-label" style="left:15px">Choose Your<br>Loan Amount</p>
  <p class="abs step-label" style="left:227px">Quick and<br>Easy</p>
  <p class="abs step-label" style="left:434px;width:190px">Available In<br>24 Hours or Less</p>

  <div class="abs cta">Contact Us Today!</div>

  <div class="abs footer-phone"><span class="contact-icon"><svg width="20" height="20" viewBox="0 0 24 24"><path d="M6 2l4 4-2 3c1 3 4 6 7 7l3-2 4 4-3 4C10 22 2 14 2 5z" fill="none" stroke="var(--green)" stroke-width="2"/></svg></span>555-014-2290</div>
  <div class="abs footer-divider"></div>
  <div class="abs footer-address"><span class="contact-icon"><svg width="18" height="18" viewBox="0 0 24 24"><path d="M12 22s-7-7-7-12a7 7 0 0 1 14 0c0 5-7 12-7 12z" fill="none" stroke="var(--green)" stroke-width="2"/><circle cx="12" cy="10" r="2.5" fill="none" stroke="var(--red)" stroke-width="2"/></svg></span><span>Compliance Department<br>4120 HARLOW AVE SUITE 210<br>Riverton, TX 78000</span></div>
</div>
</body>
</html>
```